Bright And Steady Web Design & Marketing

Will award a 2nd place prize of $100.00 if someone can come up with a logo to match this design!
Updates

Okay, I'm really looking to see some better designs here. What do you think will bring the best designs out? Please remember with all future submissions I'm looking for a cartoon style / illustrator style website. I'm not sure what the technical term is for it, so I uploaded some images in the brief.

Target Market(s)

Small Business Owners

Industry/Entity Type

Marketing

Logo Text

BrightAndSteady.example

Number of Pages Required

1 page

Colors

Designer to choose colors to be used in the design.

Requirements
Must have
• Logo should say BrightAndSteady.example I would like more than just a text logo. I want some sort of cool custom graphic / icon with it that will look nice on shirts/hats/etc

```html
<!DOCTYPE html>
<html lang="en">
<head>
<meta charset="utf-8">
<title>BrightAndSteady.example – Web Design &amp; Marketing</title>
<link href="https://fonts.googleapis.com/css2?family=Cinzel:wght@400;700&family=Roboto:wght@400;500;700&family=Roboto+Condensed:wght@400;700&family=Tinos:wght@400;700&display=swap" rel="stylesheet">
<style>
:root{
  --blue:#1b6fc2;
  --blue-dark:#11508f;
  --orange:#ef7d0b;
  --ink:#222831;
  --text:#4a4f57;
  --muted:#8a9099;
  --dark:#1d2229;
  --beige:#f6f4ef;
  --sky:#dde9f5;
  --line:#d9dde2;
  --white:#ffffff;
}
*{box-sizing:border-box;margin:0;padding:0}
html,body{width:1200px;height:4455px;overflow:hidden;background:var(--white)}
body{font-family:"Roboto",Arial,sans-serif;color:var(--text)}
.page{position:relative;width:1200px;height:4455px;overflow:hidden}
.block{position:absolute;left:0;width:1200px}
.title{font-family:"Cinzel",Georgia,serif;font-weight:700;text-align:center;color:var(--ink);font-size:31px;letter-spacing:1.5px}
.lead{font-family:"Tinos",Georgia,serif;font-size:13px;line-height:1.55;text-align:center;color:var(--text);width:900px;margin:0 auto}
.fill{position:absolute}

/* header */
.header{top:0;height:89px;background:var(--white)}
.brand{position:absolute;left:150px;top:24px;display:flex;align-items:center;gap:10px}
.brand-dot{width:14px;height:14px;border-radius:50%;background:var(--orange)}
.brand-name{font-family:"Tinos",Georgia,serif;font-weight:700;font-size:28px;color:var(--blue-dark)}
.phone{position:absolute;right:138px;top:28px;display:flex;align-items:center;gap:8px;font-family:"Roboto Condensed",sans-serif;font-size:27px;color:var(--blue-dark)}
.nav{top:89px;height:30px;background:var(--blue);display:flex;padding-left:145px}
.nav a{display:block;font-family:"Roboto Condensed",sans-serif;font-size:15px;color:var(--white);text-decoration:none;line-height:30px;padding:0 30px;margin-right:58px;text-transform:uppercase}
.nav a.active{background:var(--orange)}

/* hero */
.hero{top:119px;height:475px}
.hero-art{left:0;top:0;width:1200px;height:475px;background:linear-gradient(180deg,#f3f4f4 0%,#e4e7e8 55%,#c9cdcf 100%)}
.hero-arrow{position:absolute;top:232px;width:22px;height:22px;background:#333;color:#fff;font-size:14px;text-align:center;line-height:22px}
.hero-bar{position:absolute;left:0;bottom:0;width:1200px;height:58px;background:rgba(30,34,40,.82);display:flex;align-items:center;justify-content:center;gap:18px}
.hero-bar p{font-family:"Roboto Condensed",sans-serif;font-size:21px;font-weight:700;color:var(--white)}
.btn-call{display:flex;align-items:center;gap:7px;padding:7px 14px;background:var(--blue);color:#fff;font-family:"Roboto Condensed",sans-serif;font-size:19px}

/* about */
.about{top:594px;height:640px}
.about .title{margin-top:52px}
.about .title span{color:var(--orange);font-family:"Tinos",Georgia,serif;font-size:24px;letter-spacing:0}
.about .lead{margin-top:26px;width:920px;font-size:12.5px}
.video{left:432px;top:232px;width:336px;height:303px;background:linear-gradient(180deg,#2b2f35 0%,#4a4f56 8%,#e8eaec 12%,#d6d9dc 80%,#b9bdc2 100%);border-radius:10px}
.btn-grey{position:absolute;left:502px;top:542px;width:196px;height:46px;background:#5e6064;color:#fff;display:flex;align-items:center;justify-content:center;gap:8px;font-family:"Roboto Condensed",sans-serif;font-size:21px}

/* services */
.services{top:1234px;height:760px;background:var(--dark)}
.services-art{left:0;top:0;width:1200px;height:760px;background:linear-gradient(180deg,#1c2a33 0%,#242a31 45%,#3a2f2a 100%)}
.services .title{position:relative;color:#fff;margin-top:50px}
.services .lead{position:relative;color:#d6d9dd;margin-top:20px}
.diagram{position:absolute;left:0;top:0}
.svc{position:absolute;width:200px;font-size:11px;line-height:1.35;color:#e1e3e6}
.svc h4{font-size:12.5px;font-weight:500;margin-bottom:3px}
.svc.r{text-align:right}

/* plans */
.plans{top:1994px;height:650px;background:var(--white)}
.plans .title{margin-top:52px}
.floor{left:0;top:490px;width:1200px;height:160px;background:linear-gradient(180deg,#e9ddcb 0%,#c8a27a 30%,#a97a4e 100%)}
.card{position:absolute;width:172px;background:#fff;border:1px solid #e3e3e3;border-top:3px solid var(--orange);box-shadow:0 4px 12px rgba(0,0,0,.15);text-align:center;padding-top:22px}
.card .ico{width:44px;height:44px;border-radius:50%;border:2px solid #c9ced4;margin:0 auto;display:flex;align-items:center;justify-content:center}
.card h3{font-size:14px;font-weight:500;color:var(--ink);margin-top:14px;padding-bottom:20px;border-bottom:1px solid #eee}
.card .from{font-family:"Tinos",serif;font-size:11px;color:var(--muted);margin-top:16px}
.card .price{font-family:"Roboto Condensed",sans-serif;font-size:38px;color:#555;line-height:1.1}
.card .price sup{font-size:14px;vertical-align:top;position:relative;top:6px}
.card .price small{font-size:14px}
.card.basic .price{color:var(--orange)}
.card ul{list-style:none;text-align:left;margin:22px 0 0 26px;font-size:10.5px;color:var(--text)}
.card li{margin-bottom:9px}
.card li::before{content:"›";color:var(--muted);margin-right:8px}
.card .go{display:inline-block;margin-top:10px;width:114px;height:26px;line-height:26px;background:#555;color:#fff;font-size:12px}
.card.basic .go{background:var(--orange)}
.card .more{font-size:10.5px;color:#333;margin:8px 0 14px}

/* clients */
.clients{top:2644px;height:268px;background:var(--beige)}
.clients .title{margin-top:40px}
.clients .lead{margin-top:16px}
.logo-row{position:absolute;left:150px;top:192px;width:900px;display:flex;justify-content:space-between;align-items:center}
.client{display:flex;align-items:center;gap:5px;font-family:"Roboto",sans-serif;font-size:15px;font-weight:500;color:#2b2f35}
.client i{display:block;width:11px;height:11px;border-radius:50%;background:#2b2f35}
.row-arrow{position:absolute;top:188px;font-size:26px;color:#999}

/* why */
.why{top:2912px;height:520px;background:var(--sky)}
.why .title{margin-top:60px}
.why .lead{margin-top:20px}
.feat{position:absolute;width:230px;font-size:11px;line-height:1.35;color:var(--text)}
.feat h4{font-size:12.5px;font-weight:500;color:var(--blue-dark)}
.feat.orange h4{color:var(--orange)}
.feat.r{text-align:right}

/* team */
.team{top:3432px;height:340px;background:#fff}
.team .title{margin-top:62px}
.team .lead{margin-top:16px}
.member{position:absolute;top:176px;width:404px;height:132px}
.member .photo{position:absolute;left:0;top:0;width:74px;height:72px;border:3px solid #fff;box-shadow:0 1px 4px rgba(0,0,0,.25);background:linear-gradient(180deg,#c8ccd2,#8b939c)}
.member .card-box{position:absolute;left:30px;top:20px;width:374px;height:50px;border:1px solid var(--line);padding:8px 0 0 64px}
.member h4{font-size:13px;font-weight:700;color:#2a2f36}
.member h5{font-size:12px;font-weight:400;color:var(--blue)}
.member p{position:absolute;left:30px;top:84px;width:370px;font-size:11px;line-height:1.4;color:var(--text)}
.team .row-arrow{top:234px}

/* inquiry */
.inquiry{top:3772px;height:386px;background:linear-gradient(180deg,#fafafa,#f1f1f1)}
.inquiry-art{left:0;top:0;width:470px;height:386px;background:linear-gradient(120deg,#eceeef 0%,#dfe3e6 55%,#c6ccd1 100%)}
.inquiry .title{position:absolute;left:490px;top:46px;text-align:left}
.field{position:absolute;height:30px;border-bottom:1px solid #c9ced4;font-size:11px;color:#555}
.field.area{border:1px solid #c9ced4;background:#fff}
.area-label{position:absolute;font-size:11px;color:#555}
.submit{position:absolute;left:510px;top:4105px;left:510px}
.btn-submit{position:absolute;left:510px;top:334px;width:72px;height:24px;background:var(--blue-dark);color:#fff;font-size:11px;text-align:center;line-height:24px;font-weight:700}

/* footer */
.footer{top:4158px;height:268px;background:#1b2230}
.footer-art{left:0;top:0;width:1200px;height:268px;background:linear-gradient(180deg,#222b3a 0%,#1a212d 60%,#141921 100%)}
.fcol{position:absolute;top:34px;font-size:11px;color:#e3e6ea;line-height:1.75}
.fcol h4{font-size:13px;font-weight:500;color:#fff;margin-bottom:8px}
.fcol h4 span{color:var(--orange)}
.fcol ul{list-style:none}
.fcol li::before{content:"› ";color:#aaa}
.news-input{width:210px;height:22px;background:#fff;margin-top:10px;color:#555;padding-left:6px;font-size:11px;line-height:22px}
.btn-sub{display:inline-block;margin-top:8px;padding:0 10px;height:22px;line-height:22px;background:var(--blue);color:#fff;font-size:12px;font-weight:700}
.copy{top:4426px;height:29px;background:var(--blue-dark);color:#e8eef6;font-size:11px;line-height:29px}
.copy .l{position:absolute;left:150px}
.copy .r{position:absolute;right:150px}
</style>
</head>
<body>
<div class="page">

  <header class="block header">
    <div class="brand"><span class="brand-dot"></span><span class="brand-name">BrightAndSteady.example</span></div>
    <div class="phone">
      <svg width="28" height="28" viewBox="0 0 28 28"><circle cx="14" cy="14" r="12.5" fill="none" stroke="#11508f" stroke-width="2"/><path d="M10 8l3 3-2 2c1 2 2 3 4 4l2-2 3 3-2 2c-5 0-10-5-10-10z" fill="#11508f"/></svg>
      <span>555-010-2030</span>
    </div>
  </header>

  <nav class="block nav">
    <a class="active">Home</a><a>Services &amp; Pricing</a><a>Our Team</a><a>Clients</a><a>Contact Us</a>
  </nav>

  <section class="block hero">
    <div class="fill hero-art" role="img" aria-label="Desk scene with a plant and a hand-drawn web design sketch with notes on research, product, logo and creativity"></div>
    <div class="hero-arrow" style="left:0">‹</div>
    <div class="hero-arrow" style="right:0">›</div>
    <div class="hero-bar">
      <p>The Design &amp; Marketing Team That Always Puts Honesty &amp; Care Before Profits</p>
      <div class="btn-call"><svg width="16" height="16" viewBox="0 0 16 16"><path d="M3 1l3 3-2 2c1 2 3 4 5 5l2-2 3 3-2 3C6 15 1 10 1 3z" fill="#fff"/></svg>Call Us Today</div>
    </div>
  </section>

  <section class="block about">
    <h2 class="title">About <span>BrightAndSteady.example</span></h2>
    <p class="lead">We believe that honesty and integrity come before personal profits. We are a family owned and operated company. Our parents raised us to take care of each other and that's exactly what we've done. We treat each of our clients with the same loyalty and respect that we give each other.<br>We are not looking to have hundreds and thousands of clients. We are looking to expand our family with a handful of like-minded individuals. Companies who take pride in their work and their customers. We want to build mutually beneficial, lucrative, and long term partnerships.</p>
    <div class="fill video" role="img" aria-label="Laptop showing the company introduction video with a play button"></div>
    <div class="btn-grey"><svg width="18" height="18" viewBox="0 0 16 16"><path d="M3 1l3 3-2 2c1 2 3 4 5 5l2-2 3 3-2 3C6 15 1 10 1 3z" fill="#fff"/></svg>Call Us Today</div>
  </section>

  <section class="block services">
    <div class="fill services-art" role="img" aria-label="Dark cartoon street scene with people and shop signs behind the services diagram"></div>
    <h2 class="title">Services We Provide</h2>
    <p class="lead">Lorem ipsum dolor sit amet, consectetuer adipiscing elit, sed diam nonummy nibh euismod tincidunt ut laoreet dolore magna aliquam erat volutpat. Ut wisi enim ad minim veniam, quis nostrud exerci.</p>
    <svg class="diagram" width="1200" height="760" viewBox="0 0 1200 760">
      <circle cx="602" cy="402" r="175" fill="none" stroke="#cfd3d8" stroke-width="2" stroke-dasharray="3 6"/>
      <circle cx="602" cy="402" r="72" fill="none" stroke="#ffffff" stroke-opacity=".25" stroke-width="2"/>
      <g font-family="Roboto,Arial,sans-serif" font-size="14" font-weight="700" fill="#fff" text-anchor="middle">
        <circle cx="661" cy="228" r="30" fill="#1aa6d6"/><circle cx="690" cy="190" r="14" fill="#1aa6d6" stroke="#fff" stroke-width="2"/><text x="690" y="195">1</text>
        <circle cx="751" cy="285" r="30" fill="#8cc63f"/><circle cx="793" cy="318" r="14" fill="#8cc63f" stroke="#fff" stroke-width="2"/><text x="793" y="323">2</text>
        <circle cx="777" cy="416" r="30" fill="#9b3fc9"/><circle cx="760" cy="455" r="14" fill="#9b3fc9" stroke="#fff" stroke-width="2"/><text x="760" y="460">3</text>
        <circle cx="731" cy="520" r="30" fill="#e8501e"/><circle cx="778" cy="524" r="14" fill="#e8501e" stroke="#fff" stroke-width="2"/><text x="778" y="529">4</text>
        <circle cx="602" cy="580" r="30" fill="#1e7fd0"/><circle cx="640" cy="572" r="14" fill="#1e7fd0" stroke="#fff" stroke-width="2"/><text x="640" y="577">5</text>
        <circle cx="463" cy="540" r="30" fill="#19a9b8"/><circle cx="494" cy="608" r="14" fill="#19a9b8" stroke="#fff" stroke-width="2"/><text x="494" y="613">6</text>
        <circle cx="422" cy="430" r="30" fill="#c2d82a"/><circle cx="440" cy="484" r="14" fill="#c2d82a" stroke="#fff" stroke-width="2"/><text x="440" y="489">7</text>
        <circle cx="432" cy="300" r="30" fill="#fff" stroke="#d5d8dc" stroke-width="2"/><circle cx="388" cy="346" r="14" fill="#2e9b4a" stroke="#fff" stroke-width="2"/><text x="388" y="351">8</text>
        <circle cx="540" cy="225" r="30" fill="#f39c12"/><circle cx="486" cy="203" r="14" fill="#f39c12" stroke="#fff" stroke-width="2"/><text x="486" y="208">9</text>
      </g>
      <g fill="none" stroke="#fff" stroke-width="2.5">
        <rect x="649" y="216" width="24" height="18" rx="2"/>
        <path d="M741 293l10-16 10 16z"/>
        <rect x="767" y="406" width="20" height="20" rx="3"/>
        <path d="M721 528l20-16M725 512h16v16"/>
        <circle cx="598" cy="576" r="8"/><path d="M604 582l8 8"/>
        <circle cx="463" cy="540" r="10"/><circle cx="463" cy="540" r="3"/>
        <path d="M412 420h20v16h-20zM418 436v6M426 436v6"/>
        <rect x="424" y="290" width="16" height="20" stroke="#555"/>
        <path d="M530 232l10-16 10 16"/>
      </g>
    </svg>
    <div class="svc r" style="left:285px;top:164px"><h4 style="color:#f39c12">Consulting Service</h4>Duis autem vel eum iriure dolor in hendrerit in vulputate velit consequat.</div>
    <div class="svc" style="left:730px;top:164px"><h4 style="color:#1aa6d6">Website Design &amp; Management</h4>Duis autem vel eum iriure dolor in hendrerit in vulputate velit consequat.</div>
    <div class="svc r" style="left:150px;top:277px"><h4 style="color:#2e9b4a">Outsourcing Management</h4>Duis autem vel eum iriure dolor in hendrerit in vulputate velit consequat.</div>
    <div class="svc" style="left:826px;top:268px"><h4 style="color:#8cc63f">Logo Design &amp; Branding Materials</h4>Duis autem vel eum iriure dolor in hendrerit in vulputate velit consequat.</div>
    <div class="svc r" style="left:190px;top:406px"><h4 style="color:#c2d82a">Marketing Material &amp; Print Design</h4>Duis autem vel eum iriure dolor in hendrerit in vulputate velit consequat.</div>
    <div class="svc" style="left:818px;top:390px"><h4 style="color:#9b3fc9">Infographic Design &amp; Development</h4>Duis autem vel eum iriure dolor in hendrerit in vulputate.</div>
    <div class="svc r" style="left:195px;top:533px"><h4 style="color:#2fb36a">Social Media Marketing</h4>Duis autem vel eum iriure dolor in hendrerit in vulputate velit consequat.</div>
    <div class="svc" style="left:812px;top:510px"><h4 style="color:#e8501e">Local Seo Management</h4>Duis autem vel eum iriure dolor in hendrerit in vulputate velit consequat.</div>
    <div class="svc" style="left:650px;top:614px"><h4 style="color:#1e9be0">Search Engine Optimization</h4>Duis autem vel eum iriure dolor in hendrerit in vulputate velit consequat.</div>
  </section>

  <section class="block plans">
    <div class="fill floor" role="img" aria-label="Wooden floor under the pricing cards"></div>
    <h2 class="title">Select Your Plan</h2>
    <div class="card basic" style="left:199px;top:144px">
      <div class="ico"><svg width="20" height="20" viewBox="0 0 20 20"><path d="M4 16l12-12M10 4h6v6" stroke="#1b6fc2" stroke-width="2.5" fill="none"/></svg></div>
      <h3>Basic Plan</h3><div class="from">Starting from</div>
      <div class="price"><sup>$</sup>52<small>.95</small></div>
      <ul><li>Lorem Ipsum Dolar Ipsum</li><li>Lorem Ipsum Dolar</li><li>Lorem Ipsum Dolar Ipsum</li><li>Lorem Ipsum Dolar</li></ul>
      <div class="go">Get Started &nbsp;→</div><div class="more">More information</div>
    </div>
    <div class="card" style="left:395px;top:128px">
      <div class="ico"><svg width="20" height="20" viewBox="0 0 20 20"><rect x="3" y="4" width="14" height="12" fill="none" stroke="#555" stroke-width="2"/><path d="M3 8h14" stroke="#555" stroke-width="2"/></svg></div>
      <h3>Standard Plan</h3><div class="from">Starting from</div>
      <div class="price"><sup>$</sup>114<small>.00</small></div>
      <ul><li>Lorem Ipsum Dolar Ipsum</li><li>Lorem Ipsum Dolar</li><li>Lorem Ipsum Dolar Ipsum</li><li>Lorem Ipsum Dolar</li></ul>
      <div class="go">Get Started &nbsp;→</div><div class="more">More information</div>
    </div>
    <div class="card" style="left:594px;top:144px">
      <div class="ico"><svg width="20" height="20" viewBox="0 0 20 20"><circle cx="10" cy="10" r="6" fill="none" stroke="#ef7d0b" stroke-width="2.5"/></svg></div>
      <h3>Gold Plan</h3><div class="from">Starting from</div>
      <div class="price"><sup>$</sup>200<small>.95</small></div>
      <ul><li>Lorem Ipsum Dolar Ipsum</li><li>Lorem Ipsum Dolar</li><li>Lorem Ipsum Dolar Ipsum</li><li>Lorem Ipsum Dolar</li></ul>
      <div class="go">Get Started &nbsp;→</div><div class="more">More information</div>
    </div>
    <div class="card" style="left:796px;top:144px">
      <div class="ico"><svg width="20" height="20" viewBox="0 0 20 20"><circle cx="9" cy="9" r="5" fill="none" stroke="#1b6fc2" stroke-width="2.5"/><path d="M13 13l4 4" stroke="#1b6fc2" stroke-width="2.5"/></svg></div>
      <h3>Platinum Plan</h3><div class="from">Starting from</div>
      <div class="price"><sup>$</sup>490<small>.00</small></div>
      <ul><li>Lorem Ipsum Dolar Ipsum</li><li>Lorem Ipsum Dolar</li><li>Lorem Ipsum Dolar Ipsum</li><li>Lorem Ipsum Dolar</li></ul>
      <div class="go">Get Started &nbsp;→</div><div class="more">More information</div>
    </div>
  </section>

  <section class="block clients">
    <h2 class="title">Our Clients</h2>
    <p class="lead">Lorem ipsum dolor sit amet, consectetuer adipiscing elit, sed diam nonummy nibh euismod tincidunt ut laoreet dolore magna aliquam erat volutpat. Ut wisi enim ad minim veniam, quis nostrud exerci.</p>
    <div class="row-arrow" style="left:112px">‹</div>
    <div class="logo-row">
      <span class="client"><i></i>Linden</span>
      <span class="client">Corvale</span>
      <span class="client">Corvale</span>
      <span class="client">Nodewick</span>
      <span class="client"><i></i>Linden</span>
      <span class="client"><i></i>Gentrum</span>
      <span class="client">Arcbay</span>
      <span class="client">Arcbay</span>
    </div>
    <div class="row-arrow" style="right:112px">›</div>
  </section>

  <section class="block why">
    <h2 class="title">Why Choose Us</h2>
    <p class="lead">Lorem ipsum dolor sit amet, consectetuer adipiscing elit, sed diam nonummy nibh euismod tincidunt ut laoreet dolore magna aliquam erat volutpat. Ut wisi enim ad minim veniam, quis nostrud exerci.</p>
    <svg class="diagram" width="1200" height="520" viewBox="0 0 1200 520">
      <path d="M428 248 A185 185 0 0 1 778 248" fill="none" stroke="#c6d3e0" stroke-width="2" stroke-dasharray="3 5"/>
      <path d="M470 345 A185 185 0 0 0 740 345" fill="none" stroke="#c6d3e0" stroke-width="2" stroke-dasharray="3 5"/>
      <polygon points="580,270 626,270 658,302 658,348 626,380 580,380 548,348 548,302" fill="#1b6fc2" stroke="#fff" stroke-width="5"/>
      <circle cx="424" cy="245" r="19" fill="#ef7d0b"/><circle cx="424" cy="245" r="24" fill="none" stroke="#ef7d0b" stroke-opacity=".35" stroke-width="4"/>
      <circle cx="486" cy="340" r="19" fill="#1b6fc2"/>
      <circle cx="606" cy="385" r="19" fill="#1b6fc2"/>
      <circle cx="783" cy="245" r="19" fill="#1b6fc2"/>
      <circle cx="731" cy="336" r="19" fill="#1b6fc2"/>
      <g fill="none" stroke="#fff" stroke-width="2.2">
        <path d="M416 245h16M424 237v16"/>
        <rect x="478" y="334" width="16" height="11"/>
        <circle cx="606" cy="385" r="8"/><path d="M606 380v5h4"/>
        <rect x="775" y="239" width="16" height="12"/>
        <path d="M723 340l4-8h8l4 8z"/>
      </g>
    </svg>
    <div class="feat orange r" style="left:170px;top:228px"><h4>100% Risk Free Investment</h4>Lorem ipsum dolor sit amet, consectetuer adipiscing elit, sed diam.</div>
    <div class="feat r" style="left:232px;top:326px"><h4>Customer Loyalty Program</h4>Lorem ipsum dolor sit amet, consectetuer adipiscing elit, sed diam.</div>
    <div class="feat" style="left:492px;top:418px;text-align:center"><h4>24/7 U.S. Based Customer Support</h4>Lorem ipsum dolor sit amet, consectetuer adipiscing elit, sed diam.</div>
    <div class="feat" style="left:812px;top:228px"><h4>Multiple Payment Options Available</h4>Lorem ipsum dolor sit amet, consectetuer adipiscing elit, sed diam.</div>
    <div class="feat" style="left:760px;top:320px"><h4>Unmatched Personal Service</h4>Lorem ipsum dolor sit amet, consectetuer adipiscing elit, sed diam.</div>
  </section>

  <section class="block team">
    <h2 class="title">Our Team</h2>
    <p class="lead">Lorem ipsum dolor sit amet, consectetuer adipiscing elit, sed diam nonummy nibh euismod tincidunt ut laoreet dolore magna aliquam erat volutpat. Ut wisi enim ad minim veniam, quis nostrud exerci.</p>
    <div class="row-arrow" style="left:112px">‹</div>
    <div class="member" style="left:168px">
      <div class="card-box"><h4>DANIEL FERRO</h4><h5>Chief Executive Officer</h5></div>
      <div class="photo" role="img" aria-label="Portrait photo of the chief executive officer"></div>
      <p>Lorem ipsum dolor sit amet, consectetuer adipiscing elit, sed diam nonummy nibh euismod tincidunt ut laoreet dolore magna aliquam. [...]</p>
    </div>
    <div class="member" style="left:632px">
      <div class="card-box"><h4>OWEN HALE</h4><h5>Chief Operations Officer</h5></div>
      <div class="photo" role="img" aria-label="Portrait photo of the chief operations officer"></div>
      <p>Lorem ipsum dolor sit amet, consectetuer adipiscing elit, sed diam nonummy nibh euismod tincidunt ut laoreet dolore magna aliquam. [...]</p>
    </div>
    <div class="row-arrow" style="right:112px">›</div>
  </section>

  <section class="block inquiry">
    <div class="fill inquiry-art" role="img" aria-label="Hands typing on a laptop beside a coffee mug and a small plant"></div>
    <h2 class="title">Quick Inquiry</h2>
    <div class="field" style="left:492px;top:104px;width:258px">First Name</div>
    <div class="field" style="left:768px;top:104px;width:252px">Last Name</div>
    <div class="field" style="left:492px;top:152px;width:258px">Email</div>
    <div class="field" style="left:768px;top:152px;width:252px">Phone Number</div>
    <div class="area-label" style="left:492px;top:200px">Details About Your Enquiry</div>
    <div class="field area" style="left:492px;top:238px;width:528px;height:70px"></div>
    <div class="btn-submit">SUBMIT</div>
  </section>

  <footer class="block footer">
    <div class="fill footer-art" role="img" aria-label="Night city skyline behind the footer"></div>
    <div class="fcol" style="left:150px"><h4>Quick <span>Links</span></h4>
      <ul><li>Home</li><li>Services</li><li>Pricing</li><li>Our Team</li><li>Success Stories</li><li>Clients</li><li>Contact Us</li></ul></div>
    <div class="fcol" style="left:345px"><h4>Contact <span>Details</span></h4>
      <b>BrightAndSteady.example</b><br>Street Name, City Name<br>State Zipcode<br>☎ 555-010-4560<br>✆ 555-010-4560<br>✉ inquiry@brightandsteady.example</div>
    <div class="fcol" style="left:615px"><h4>Newsletter <span>Signup</span></h4>
      Lorem ipsum dolor sit amet, consectetuer<br>adipiscing elit, sed diam.
      <div class="news-input">Email</div>
      <div class="btn-sub">Subscribe</div></div>
  </footer>

  <div class="block copy"><span class="l">Copyright © 2017 BrightAndSteady.example. All rights reserved.</span><span class="r">Terms of Use | Privacy Policy</span></div>

</div>
</body>
</html>
```